KRV Business Cards

We are a local commercial development company based in Silicon Valley and we would like a new business card. I've attached a copy of our company brochure to give a flavor of what we do, our logo, info company colors/graphics, and our current business card. We don't necessarily need a crazy makeover, but would like something that feels a little bit more "fresh" and modern (we've had the same business card design for 15+ years), but still in keeping with our overall brand -- clean, high-quality, modern but timeless. Would like to add our website to the info on the card (www.velmara.com) and would like the flexibility for some folks to have an efax number listed and some not to have that included (without it looking like there is a hole).

```html
<!DOCTYPE html>
<html lang="en">
<head>
<meta charset="utf-8">
<title>KRV Business Cards</title>
<link rel="stylesheet" href="https://fonts.googleapis.com/css2?family=Cinzel:wght@400;500&display=swap">
<style>
  :root {
    --navy: #34526f;
    --grey: #7b7b7a;
    --white: #ffffff;
    --ink: #2b2b2b;
    --page: #eceae6;
    --text-font: "Cinzel", serif;
  }
  * { box-sizing: border-box; margin: 0; padding: 0; }
  html, body { width: 1200px; height: 1200px; overflow: hidden; background: var(--page); }
  body { font-family: var(--text-font); position: relative; }

  .card {
    position: absolute;
    left: 170px;
    width: 860px;
    height: 491px;
    background: var(--white);
    box-shadow: 0 6px 18px rgba(0,0,0,.18);
    overflow: hidden;
  }
  .card--back { top: 60px; }
  .card--front { top: 620px; }

  /* Back: block pattern */
  .block { position: absolute; background: var(--navy); }
  .rule { position: absolute; left: 0; right: 0; height: 3px; background: var(--navy); }

  .brand {
    position: absolute;
    display: flex;
    align-items: center;
    gap: 14px;
    color: var(--navy);
  }
  .brand__dot {
    width: 54px; height: 54px; border-radius: 50%;
    border: 7px solid var(--navy); flex: none;
  }
  .brand__name {
    font-size: 17px; line-height: 1.15; letter-spacing: .28em; text-transform: uppercase;
  }
  .card--back .brand { left: 322px; top: 208px; }

  /* Front */
  .front__logo-zone { position: absolute; left: 0; top: 0; width: 460px; height: 185px; }
  .card--front .brand { left: 40px; top: 40px; }
  .card--front .brand__dot { width: 74px; height: 74px; border-width: 9px; }
  .card--front .brand__name { font-size: 21px; }
  .front__name-panel {
    position: absolute; left: 476px; top: 0; right: 0; height: 185px;
    background: var(--grey);
    display: flex; flex-direction: column; align-items: center; justify-content: center;
    color: var(--ink); text-align: center;
  }
  .person__name { font-size: 24px; letter-spacing: .16em; text-transform: uppercase; }
  .person__title { font-size: 15px; letter-spacing: .14em; text-transform: uppercase; margin-top: 6px; }
  .front__divider { position: absolute; left: 460px; top: 0; width: 16px; height: 185px; background: var(--white); }
  .front__band {
    position: absolute; left: 0; right: 0; top: 205px; bottom: 0;
    background: var(--navy); color: var(--white);
  }
  .front__stripe { position: absolute; left: 0; right: 0; top: 188px; height: 6px; background: var(--navy); }
  .contact { position: absolute; left: 40px; top: 34px; font-size: 15px; letter-spacing: .06em; }
  .contact__row { display: flex; align-items: center; gap: 12px; margin-bottom: 14px; }
  .contact__row svg { width: 16px; height: 16px; flex: none; }
  .contact__lower { text-transform: lowercase; font-size: 14px; }
  .phones { position: absolute; right: 60px; bottom: 36px; font-size: 15px; line-height: 1.7; }
  .phones dt { display: inline-block; width: 70px; }
  .phones dd { display: inline; }
  .band__line { position: absolute; left: 0; right: 0; bottom: 20px; height: 4px; background: var(--white); }
</style>
</head>
<body>

<section class="card card--back" aria-label="Card back">
  <div class="block" style="left:0;top:0;width:300px;height:88px"></div>
  <div class="block" style="left:318px;top:0;width:200px;height:88px"></div>
  <div class="block" style="left:536px;top:0;width:324px;height:88px"></div>
  <div class="rule" style="top:104px"></div>
  <div class="block" style="left:0;top:124px;width:276px;height:140px"></div>
  <div class="block" style="left:612px;top:124px;width:248px;height:140px"></div>
  <div class="rule" style="top:292px"></div>
  <div class="block" style="left:0;top:312px;width:300px;height:179px"></div>
  <div class="block" style="left:318px;top:336px;width:200px;height:155px"></div>
  <div class="block" style="left:536px;top:312px;width:324px;height:179px"></div>
  <div class="brand">
    <span class="brand__dot"></span>
    <span class="brand__name">Kervale<br>Development<br>Company</span>
  </div>
</section>

<section class="card card--front" aria-label="Card front">
  <div class="front__logo-zone">
    <div class="brand">
      <span class="brand__dot"></span>
      <span class="brand__name">Kervale<br>Development<br>Company</span>
    </div>
  </div>
  <div class="front__divider"></div>
  <div class="front__name-panel">
    <p class="person__name">Ellen J. Marsh</p>
    <p class="person__title">Partner</p>
  </div>
  <div class="front__stripe"></div>
  <div class="front__band">
    <div class="contact">
      <p class="contact__row">
        <svg viewBox="0 0 16 16" aria-hidden="true"><path d="M8 1a5 5 0 0 0-5 5c0 4 5 9 5 9s5-5 5-9a5 5 0 0 0-5-5zm0 7a2 2 0 1 1 0-4 2 2 0 0 1 0 4z" fill="#fff"/></svg>
        <span>Linden Avenue, Menlo Park, California 94025</span>
      </p>
      <p class="contact__row">
        <svg viewBox="0 0 16 16" aria-hidden="true"><rect x="1" y="3" width="14" height="10" fill="#fff"/><path d="M1 3l7 6 7-6" stroke="#34526f" stroke-width="1.4" fill="none"/></svg>
        <span class="contact__lower">ellen@velmara.com</span>
      </p>
      <p class="contact__row">
        <svg viewBox="0 0 16 16" aria-hidden="true"><circle cx="8" cy="8" r="6.3" fill="none" stroke="#fff" stroke-width="1.4"/><ellipse cx="8" cy="8" rx="2.6" ry="6.3" fill="none" stroke="#fff" stroke-width="1.2"/><path d="M1.7 8h12.6" stroke="#fff" stroke-width="1.2"/></svg>
        <span class="contact__lower">www.velmara.com</span>
      </p>
    </div>
    <dl class="phones">
      <div><dt>Direct</dt><dd>: 6505550142</dd></div>
      <div><dt>Main</dt><dd>: 6505550100</dd></div>
      <div><dt>Fax</dt><dd>: 6505550199</dd></div>
    </dl>
    <div class="band__line"></div>
  </div>
</section>

</body>
</html>
```